Homepage for the brisk-trail Web Application

At the end of this text, you will find a link to a website that is under construction for a webApp that I intend to launch soon. The contest goal is for you to make redesign the homepage in a nice, fresh, modern Style. Only design, no coding necessary. It needs to have a responsive version for small screens like smart phones. Attached is the text for it, and some images that you may use. You are welcome to find or create additional supporting images. You can use PixVaultimages.com or similar service to find new images as long as I can purchase the non-exclusive use rights for the images at similar prices. The contest is just for the home page. However, the winner, if I like the work and we can agree on a fair price, could be contracted on a one-on-one basis to do the rest of the site. You are welcome to suggest minor changes like font sizes and minor variations on the Header banner, but that banner is consistent with the user interface of the application therefore should not change too much. The information should flow somewhat continually without much use of side bars or things like that.
https://www.brisk-trail-example.com
Sincerely,
Marco R. Delgado

```html
<!DOCTYPE html>
<html lang="en">
<head>
<meta charset="utf-8">
<title>Brisk Trail – Homepage Desktop &amp; Mobile</title>
<link href="https://fonts.googleapis.com/css2?family=Baloo+2:wght@600;700&family=Source+Sans+3:wght@400;600;700&display=swap" rel="stylesheet">
<style>
:root{
  --blue:#2f78c0;
  --title-blue:#1f6db6;
  --orange:#fa7b57;
  --orange-dark:#f26a44;
  --teal:#2ea3b6;
  --teal-deep:#1f8fa3;
  --cyan-light:#d8f7fb;
  --cyan-mid:#8fdbe6;
  --grey-band:#f2f2f2;
  --white:#ffffff;
  --ink:#222;
}
*{box-sizing:border-box;margin:0;padding:0}
html,body{width:752px;height:1200px;overflow:hidden;background:var(--white)}
body{font-family:"Source Sans 3",Arial,sans-serif;color:var(--ink);position:relative}
.view-label{position:absolute;top:150px;font-size:13px;letter-spacing:.5px;color:#111}
.stage{position:absolute;top:178px;transform-origin:0 0;transform:scale(.6)}
.stage--desktop{left:19px}
.stage--mobile{left:499px}
.page{position:relative;overflow:hidden;box-shadow:0 2px 8px rgba(0,0,0,.25)}
.page--desktop{width:734px;height:1173px}
.page--mobile{width:390px;height:1293px}
.abs{position:absolute}

.topbar{position:absolute;left:0;top:0;width:100%;background:var(--blue);border-bottom:3px solid var(--orange)}
.brand{position:absolute;display:flex;align-items:center;gap:6px;color:var(--white);font-family:"Source Sans 3",sans-serif;font-weight:400}
.brand__dot{width:16px;height:16px;border-radius:50%;background:var(--white)}
.nav{position:absolute;display:flex;gap:11px;font-size:10px;font-weight:600;color:var(--white)}
.login{position:absolute;display:flex;align-items:center;gap:5px;color:var(--white);font-size:10px;font-weight:600}
.login__icon{width:14px;height:14px;border-radius:50%;background:var(--white)}
.trial-tab{position:absolute;background:var(--orange);color:var(--white);font-size:10px;font-weight:600;text-align:center;border-radius:0 0 10px 10px;line-height:20px}
.burger{position:absolute;width:30px;height:22px;display:flex;flex-direction:column;justify-content:space-between}
.burger span{height:4px;background:var(--white);border-radius:1px}

.hero{position:absolute;left:0;width:100%;background:linear-gradient(160deg,var(--cyan-light) 0%,#a6e6ef 45%,#5bbdcd 100%)}
.hero__title{position:absolute;font-family:"Baloo 2",sans-serif;font-weight:700;color:var(--title-blue);line-height:1.15}
.hero__text{position:absolute;color:var(--title-blue);line-height:1.2}
.art{position:absolute;border-radius:14px}
.art--hero{background:linear-gradient(150deg,#bfeef4,#2ba3b6 60%,#1c8598)}
.art--card{background:linear-gradient(160deg,#dff6f9,#6cc7d4);border-radius:10px}
.art--round{background:radial-gradient(circle at 45% 50%,#1f6db6 0 58%,transparent 59%),linear-gradient(160deg,#dff6f9 0,#6cc7d4 100%);border-radius:50%}
.btn{position:absolute;background:var(--orange);color:var(--white);font-weight:700;text-align:center;border-radius:20px}
.dots{position:absolute;display:flex;gap:4px}
.dots i{width:9px;height:9px;border-radius:50%;background:var(--title-blue)}
.dots i.on{background:var(--orange)}
.dots--teal i{background:var(--teal)}

.intro{position:absolute;left:0;width:100%}
.intro__head{position:absolute;left:0;width:100%;text-align:center;font-family:"Baloo 2",sans-serif;font-weight:700;color:var(--orange);line-height:1.15}
.intro__sub{position:absolute;left:0;width:100%;text-align:center;font-weight:600;color:var(--title-blue);line-height:1.4}
.card{position:absolute;background:linear-gradient(135deg,var(--teal) 0%,var(--teal-deep) 100%);border-radius:10px;color:var(--white)}
.card--ghost{opacity:.35}
.card__title{position:absolute;font-weight:600;line-height:1.1}
.card__text{position:absolute;font-weight:700;line-height:1.2}
.arrow{position:absolute;width:24px;height:30px}

.why{position:absolute;left:0;width:100%;background:linear-gradient(160deg,#e6fafc 0%,#c2eff5 50%,#8fd9e4 100%)}
.why__title{position:absolute;font-family:"Baloo 2",sans-serif;font-weight:700;color:var(--title-blue)}
.why__list{position:absolute;list-style:none;color:var(--title-blue)}
.why__list li{padding-left:10px;text-indent:-9px}
.why__list li::before{content:"• "}

.footer{position:absolute;left:0;width:100%;background:var(--orange);color:var(--white)}
.footer__cols{position:absolute;display:flex;font-size:10px;line-height:1.3}
.copyright{position:absolute;left:0;width:100%;text-align:center;font-size:7px;font-weight:700}
</style>
</head>
<body>

<div class="view-label" style="left:220px">DESKTOP</div>
<div class="view-label" style="left:593px">MOBILE</div>

<!-- Desktop homepage -->
<div class="stage stage--desktop">
<main class="page page--desktop">
  <header class="topbar" style="height:48px">
    <div class="brand" style="left:18px;top:12px;font-size:17px"><span class="brand__dot"></span>Brisk Trail</div>
    <nav class="nav" style="left:249px;top:18px">
      <span>Home</span><span>About</span><span>Pricing</span><span>Blog</span><span>FAQs</span><span>Support</span><span>Reviews</span><span>Contact Us</span><span>Free-Trial</span>
    </nav>
    <div class="login" style="right:14px;top:16px">Login <span class="login__icon"></span></div>
  </header>

  <section class="hero" style="top:51px;height:320px">
    <h1 class="hero__title" style="left:91px;top:68px;font-size:29px">Find any document or<br>item instantly!</h1>
    <p class="hero__text" style="left:92px;top:146px;width:300px;font-size:14.5px">Brisk-Trail is a system that allows you to quickly search for the location of every item that you store or file.</p>
    <div class="btn" style="left:92px;top:216px;width:126px;height:30px;line-height:30px;font-size:13.5px">Learn more</div>
    <div class="art art--hero" role="img" aria-label="Illustration of a person pulling a folder from a filing cabinet built into a laptop screen" style="left:410px;top:38px;width:270px;height:262px"></div>
    <div class="dots" style="left:338px;top:300px"><i class="on"></i><i></i><i></i><i></i><i></i></div>
  </section>
  <div class="trial-tab" style="left:565px;top:48px;width:153px">Try our 30-day FREE TRIAL</div>

  <section class="intro" style="top:371px;height:430px;background:var(--grey-band)">
    <h2 class="intro__head" style="top:24px;font-size:27px">Keeping track of all your paper documents<br>and other belongings has never been easier!</h2>
    <p class="intro__sub" style="top:100px;font-size:21px">Why use a storage management system<br>like Brisk-Trail?</p>
    <svg class="arrow" style="left:128px;top:556px;margin-top:-430px" viewBox="0 0 24 30"><path d="M16 4 6 15l10 11" fill="none" stroke="var(--teal)" stroke-width="3"/></svg>
    <div class="card" style="left:158px;top:172px;width:418px;height:208px">
      <div class="art art--card" role="img" aria-label="Illustration of a person carrying a large orange document into a tall cabinet" style="left:45px;top:18px;width:140px;height:170px"></div>
      <h3 class="card__title" style="left:201px;top:37px;font-size:18px">Managing paper<br>documents</h3>
      <p class="card__text" style="left:201px;top:89px;width:180px;font-size:10px">Most people and businesses have a variety of documents that need to be filed.</p>
      <div class="btn" style="left:201px;top:142px;width:108px;height:26px;line-height:26px;font-size:12.5px">Learn more</div>
    </div>
    <svg class="arrow" style="left:582px;top:126px" viewBox="0 0 24 30"><path d="M8 4l10 11L8 26" fill="none" stroke="var(--orange)" stroke-width="3"/></svg>
    <div class="card card--ghost" style="left:615px;top:172px;width:140px;height:208px">
      <div class="art art--card" role="img" aria-label="Illustration of the next storage topic" style="left:25px;top:18px;width:100px;height:170px"></div>
    </div>
    <div class="dots" style="left:356px;top:392px"><i class="on"></i><i style="background:var(--teal)"></i></div>
  </section>
  <svg class="arrow" style="left:128px;top:628px" viewBox="0 0 24 30"><path d="M16 4 6 15l10 11" fill="none" stroke="var(--teal)" stroke-width="3"/></svg>

  <section class="why" style="top:801px;height:248px">
    <div class="art art--round" role="img" aria-label="Illustration of a person filing an orange folder into a phone-shaped cabinet" style="left:10px;top:28px;width:158px;height:180px"></div>
    <h2 class="why__title" style="left:173px;top:16px;font-size:25px">Why Brisk-Trail?</h2>
    <ul class="why__list" style="left:173px;top:52px;width:550px;font-size:14.5px;line-height:20px">
      <li>It is extremely easy to use.</li>
      <li>It Adapts to your style. Since each catalog can have 1 or more levels of depth (folders and sub-folders), Brisk-Trail does not force you to use a specific filing or storage methodology.</li>
      <li>It’s very affordable. Checkout our pricing plans!</li>
      <li>Since it is online, your data is available almost anywhere in the world.</li>
      <li>Data encryption ensures that your information is always private, safe and secure.</li>
    </ul>
    <div class="btn" style="left:173px;top:200px;width:195px;height:26px;line-height:26px;font-size:12.5px;font-weight:600">Try our 30-day FREE TRIAL</div>
  </section>

  <footer class="footer" style="top:1049px;height:124px">
    <div class="brand" style="left:205px;top:18px;font-size:16px"><span class="brand__dot"></span>Brisk Trail</div>
    <div class="footer__cols" style="left:317px;top:20px;gap:36px">
      <div style="width:44px">Sitemap<br>Workvine</div>
      <div style="width:44px">Careers<br>Chatterly</div>
      <div>Contact Us<br>Pingbird</div>
    </div>
    <p class="copyright" style="top:108px">Copyright © 2021 BriskTrail</p>
  </footer>
</main>
</div>

<!-- Mobile homepage -->
<div class="stage stage--mobile">
<main class="page page--mobile">
  <header class="topbar" style="height:44px">
    <div class="brand" style="left:16px;top:11px;font-size:15px"><span class="brand__dot"></span>Brisk Trail</div>
    <div class="burger" style="right:12px;top:10px"><span></span><span></span><span></span></div>
  </header>

  <section class="hero" style="top:47px;height:281px">
    <h1 class="hero__title" style="left:16px;top:55px;font-size:22px">Find any document<br>or item Instantly!</h1>
    <p class="hero__text" style="left:18px;top:121px;width:185px;font-size:11px">Brisk-Trail is a system that allows you to quickly search for the location of every item that you store or file.</p>
    <div class="btn" style="left:18px;top:181px;width:110px;height:26px;line-height:26px;font-size:12px">Learn more</div>
    <div class="art art--hero" role="img" aria-label="Illustration of a person pulling a folder from a filing cabinet built into a laptop screen" style="left:215px;top:55px;width:165px;height:170px"></div>
    <div class="dots" style="left:169px;top:254px"><i class="on"></i><i></i><i></i><i></i><i></i></div>
  </section>
  <div class="trial-tab" style="left:110px;top:44px;width:170px">Try our 30-day FREE TRIAL</div>

  <section class="intro" style="top:328px;height:509px;background:var(--white)">
    <h2 class="intro__head" style="top:24px;font-size:22px">Keeping track of all your paper<br>documents and other belongings<br>has never been easier!</h2>
    <p class="intro__sub" style="top:128px;font-size:18px;line-height:1.2">Why use a storage<br>management system like<br>Brisk-Trail?</p>
    <svg class="arrow" style="left:6px;top:313px" viewBox="0 0 24 30"><path d="M16 4 6 15l10 11" fill="none" stroke="var(--orange)" stroke-width="3"/></svg>
    <div class="card" style="left:31px;top:218px;width:327px;height:237px">
      <div class="art art--card" role="img" aria-label="Illustration of a person carrying a large orange document into a tall cabinet" style="left:16px;top:26px;width:150px;height:190px"></div>
      <h3 class="card__title" style="left:172px;top:34px;font-size:16px">Managing paper<br>documents</h3>
      <p class="card__text" style="left:172px;top:84px;width:125px;font-size:13px;font-weight:600;line-height:1.28">Most people and businesses have a variety of documents that need to be filed.</p>
      <div class="btn" style="left:172px;top:188px;width:106px;height:24px;line-height:24px;font-size:11.5px">Learn more</div>
    </div>
    <svg class="arrow" style="left:361px;top:313px" viewBox="0 0 24 30"><path d="M8 4l10 11L8 26" fill="none" stroke="var(--teal)" stroke-width="3"/></svg>
    <div class="dots" style="left:183px;top:478px"><i class="on"></i><i style="background:var(--teal)"></i></div>
  </section>

  <section class="why" style="top:837px;height:344px">
    <div class="art art--round" role="img" aria-label="Illustration of a person filing an orange folder into a phone-shaped cabinet" style="left:8px;top:24px;width:124px;height:190px"></div>
    <h2 class="why__title" style="left:157px;top:12px;font-size:19px">Why Brisk-Trail?</h2>
    <ul class="why__list" style="left:157px;top:43px;width:220px;font-size:10.5px;line-height:17.6px">
      <li>It is extremely easy to use.</li>
      <li>It Adapts to your style. Since each catalog can have 1 or more levels of depth (folders and sub-folders), Brisk-Trail does not force you to use a specific filing or storage methodology.</li>
      <li>It’s very affordable. Checkout our pricing plans!</li>
      <li>Since it is online, your data is available almost anywhere in the world.</li>
      <li>Data encryption ensures that your information is always private, safe and secure.</li>
    </ul>
    <div class="btn" style="left:157px;top:295px;width:173px;height:22px;line-height:22px;font-size:11px;font-weight:600">Try our 30-day FREE TRIAL</div>
  </section>

  <footer class="footer" style="top:1181px;height:112px">
    <div class="brand" style="left:52px;top:16px;font-size:14px;gap:4px"><span class="brand__dot" style="width:13px;height:13px"></span>Brisk Trail</div>
    <div class="footer__cols" style="left:150px;top:16px;gap:24px;font-size:9px">
      <div style="width:47px">Sitemap<br>Workvine</div>
      <div style="width:47px">Careers<br>Chatterly</div>
      <div>Contact Us<br>Pingbird</div>
    </div>
    <p class="copyright" style="top:95px;font-size:6px">Copyright © 2021 BriskTrail</p>
  </footer>
</main>
</div>

</body>
</html>
```